Q7 Clinic business card design

It is a doctor's business card. It will include both English and Chinese information ( will be provided). The design should look professional. It is an obstetrics and gynaecology clinic.

Target Market(s)

Hong Kong private medical market_adult females

Contact Information for Business Card

as the information provided_color coordination with the logo color

Font styles to use
Sans Serif

Colors

Designer to choose colors to be used in the design.

Requirements
Must have
• Logo.
• dr's name, credentials, address, telephone, fax no,

```html
<!DOCTYPE html>
<html lang="en">
<head>
<meta charset="utf-8">
<title>Q7 Clinic business cards</title>
<link href="https://fonts.googleapis.com/css2?family=Roboto:ital,wght@0,400;0,500;0,700;0,900;1,400&family=Noto+Sans+TC:wght@400;700&display=swap" rel="stylesheet">
<style>
  :root {
    --bg: #2b2b2c;
    --card-white: #ffffff;
    --brand-blue: #0a6fc2;
    --brand-green: #8cc63f;
    --ink-white: #ffffff;
    --logo-ink: #1b6fb8;
  }
  * { box-sizing: border-box; margin: 0; padding: 0; }
  html, body { width: 1200px; height: 1108px; overflow: hidden; }
  body {
    background: var(--bg);
    font-family: "Roboto", sans-serif;
    position: relative;
  }
  .card {
    position: absolute;
    left: 190px;
    width: 820px;
    height: 492px;
    display: flex;
    background: var(--card-white);
    box-shadow: 0 14px 30px rgba(0,0,0,0.45);
  }
  .card--chinese { top: 42px; }
  .card--english { top: 574px; }
  .card__brand {
    width: 300px;
    display: flex;
    align-items: center;
    justify-content: center;
    gap: 12px;
  }
  .brand__dot {
    width: 22px; height: 22px; border-radius: 50%;
    background: var(--brand-green);
  }
  .brand__name {
    font-family: "Roboto", sans-serif;
    font-weight: 700;
    font-size: 46px;
    color: var(--logo-ink);
    letter-spacing: 1px;
  }
  .card__info {
    flex: 1;
    color: var(--ink-white);
    padding: 58px 44px 40px 48px;
  }
  .card--chinese .card__info {
    background: var(--brand-blue);
    font-family: "Noto Sans TC", sans-serif;
  }
  .card--english .card__info { background: var(--brand-green); }

  .doctor-name { font-weight: 700; font-size: 30px; line-height: 1.2; }
  .card--english .doctor-name { font-weight: 900; font-size: 27px; letter-spacing: 0.5px; }
  .credentials { font-weight: 700; font-size: 15px; margin-top: 4px; letter-spacing: 0.5px; }
  .qualifications { font-size: 18px; line-height: 1.3; margin-top: 10px; }
  .address { font-size: 18px; line-height: 1.3; margin-top: 14px; }
  .card--english .address { font-size: 19px; }
  .address + .address { margin-top: 8px; }
  .contact { margin-top: 14px; font-size: 19px; line-height: 1.35; }
  .contact__row { display: flex; align-items: center; gap: 10px; }
  .contact__row svg { width: 18px; height: 18px; flex: none; }
  .notice { margin-top: 14px; font-size: 18px; line-height: 1.35; }
  .card--english .notice { font-style: italic; font-size: 19px; }
</style>
</head>
<body>

<section class="card card--chinese" lang="zh-Hant">
  <div class="card__brand">
    <span class="brand__dot"></span>
    <span class="brand__name">Q7 Clinic</span>
  </div>
  <div class="card__info">
    <h1 class="doctor-name">林詠詩醫生</h1>
    <p class="qualifications">
      濱海大學內外全科醫學士<br>
      濱海大學公共衞生碩士<br>
      國際婦產科學院院士<br>
      國際婦產科學院榮授院士
    </p>
    <p class="address">
      沙田大圍樂明街8號港線中心8樓803室<br>
      佐敦廣東道208號晴天廣場B座8樓816室
    </p>
    <div class="contact">
      <div class="contact__row">
        <svg viewBox="0 0 24 24" aria-hidden="true"><path fill="#fff" d="M6.6 10.8c1.4 2.8 3.8 5.1 6.6 6.6l2.2-2.2c.3-.3.7-.4 1-.2 1.1.4 2.3.6 3.6.6.6 0 1 .4 1 1V20c0 .6-.4 1-1 1C10.6 21 3 13.4 3 4c0-.6.4-1 1-1h3.5c.6 0 1 .4 1 1 0 1.3.2 2.5.6 3.6.1.3 0 .7-.2 1l-2.3 2.2z"/></svg>
        <span>23456701 ; 23456702</span>
      </div>
      <div class="contact__row">
        <svg viewBox="0 0 24 24" aria-hidden="true"><rect x="6" y="2" width="12" height="20" rx="2" fill="none" stroke="#fff" stroke-width="2"/><circle cx="12" cy="18" r="1.3" fill="#fff"/></svg>
        <span>61234567</span>
        <svg viewBox="0 0 24 24" aria-hidden="true"><rect x="7" y="3" width="10" height="6" fill="#fff"/><rect x="3" y="9" width="18" height="9" rx="2" fill="#fff"/><rect x="7" y="15" width="10" height="6" fill="#fff" stroke="#0a6fc2" stroke-width="1.5"/></svg>
        <span>23456709</span>
      </div>
    </div>
    <p class="notice">敬請預約。逢星期日及公眾假期休息。</p>
  </div>
</section>

<section class="card card--english">
  <div class="card__brand">
    <span class="brand__dot"></span>
    <span class="brand__name">Q7 Clinic</span>
  </div>
  <div class="card__info">
    <h2 class="doctor-name">DR LAM WING SZE, GRACE</h2>
    <p class="credentials">MBCHB, MPH, MRCOG, FRCOG</p>
    <p class="address">
      Unit 803, 8th floor, Harbourline Centre<br>
      8 Lok Ming Street, Tai Wai, Shatin,<br>
      New Territories
    </p>
    <p class="address">
      Unit 816, 8th floor, Tower B, Celeste Plaza<br>
      208 Canton Road, Jordan<br>
      Kowloon
    </p>
    <div class="contact">
      <div class="contact__row">
        <svg viewBox="0 0 24 24" aria-hidden="true"><path fill="#fff" d="M6.6 10.8c1.4 2.8 3.8 5.1 6.6 6.6l2.2-2.2c.3-.3.7-.4 1-.2 1.1.4 2.3.6 3.6.6.6 0 1 .4 1 1V20c0 .6-.4 1-1 1C10.6 21 3 13.4 3 4c0-.6.4-1 1-1h3.5c.6 0 1 .4 1 1 0 1.3.2 2.5.6 3.6.1.3 0 .7-.2 1l-2.3 2.2z"/></svg>
        <span>23456701 ; 23456702</span>
      </div>
      <div class="contact__row">
        <svg viewBox="0 0 24 24" aria-hidden="true"><rect x="6" y="2" width="12" height="20" rx="2" fill="none" stroke="#fff" stroke-width="2"/><circle cx="12" cy="18" r="1.3" fill="#fff"/></svg>
        <span>61234567</span>
        <svg viewBox="0 0 24 24" aria-hidden="true"><rect x="7" y="3" width="10" height="6" fill="#fff"/><rect x="3" y="9" width="18" height="9" rx="2" fill="#fff"/><rect x="7" y="15" width="10" height="6" fill="#fff" stroke="#8cc63f" stroke-width="1.5"/></svg>
        <span>23456709</span>
      </div>
    </div>
    <p class="notice">
      Consultation by appointment.<br>
      Closes on Sundays and public holidays.
    </p>
  </div>
</section>

</body>
</html>
```